Verpackungsdesign für Premium-Nahrungsergänzungsmittel
Zielgruppe
Dr. Nemo Fortal: Premium-Nahrungsergänzungsmittel für Männer über 40. Unsere Marke verkörpert Vitalität, Expertise und Lebensfreude.
Aufgabenstellung
'DR. NEMO FORTAL' ist eine Premium-Marke, die sich auf Nahrungsergänzungsmittel für Männer über 40 spezialisiert hat. Für unser erstes Produkt 'Quorabin' benötigen wir ein Verpackungsdesign, das die Essenz unserer Marke und das Potenzial des Produkts einfängt.
ZIELGRUPPE:
Männer über 40, gesundheitsbewusst und auf der Suche nach qualitativ hochwertigen, natürlich gewonnenen Nahrungsergänzungsmitteln.
UPDATE 23082023: Briefing optimiert und neu hochgeladen

```html
<!DOCTYPE html>
<html lang="de">
<head>
<meta charset="utf-8">
<title>Dr. Nemo Fortal – Quorabin Verpackung</title>
<link rel="stylesheet" href="https://fonts.googleapis.com/css2?family=Lato:wght@400;700&family=Montserrat:wght@700;800&display=swap">
<style>
:root{
  --board:#dcdcdc;
  --forest:#1f331f;
  --forest-deep:#1c2b1a;
  --moss:#3a5229;
  --moss-band:#34492a;
  --leaf:#5cb848;
  --cream:#e6e0a2;
  --ink:#1d261b;
  --white:#ffffff;
  --copy:#cfe0b0;
}
*{box-sizing:border-box;margin:0;padding:0}
html,body{width:1200px;height:1200px;overflow:hidden;background:var(--board)}
body{position:relative;font-family:"Lato",sans-serif}
.pack{position:absolute;overflow:hidden}
.pack .bg{position:absolute;inset:0;width:100%;height:100%}
.center{position:absolute;left:0;right:0;text-align:center}
.brand{font-family:"Montserrat",sans-serif;font-weight:800;letter-spacing:.01em;line-height:1}
.product{font-family:"Lato",sans-serif;font-weight:400;color:var(--white);line-height:1;letter-spacing:-.01em}
.tagline{font-weight:700;line-height:1.45;color:var(--copy)}
.weight{position:absolute;left:0;right:0;bottom:0;text-align:center;color:var(--white);font-weight:700;letter-spacing:-.02em}

/* box front */
.box-front{left:40px;top:26px;width:684px;height:476px}
.box-front .brand{top:70px;font-size:24px;color:var(--cream)}
.box-front .product{top:108px;font-size:76px}
.box-front .tagline{top:296px;font-size:18px}
.box-front .weight{height:42px;line-height:42px;font-size:19px;background:var(--moss-band)}

/* stick */
.stick{left:153px;top:634px;width:464px;height:112px}
.stick .seal{position:absolute;top:4px;bottom:0;width:36px;background:var(--forest-deep);border:1px solid #0f1a0f}
.stick .seal.l{left:0}.stick .seal.r{right:0}
.stick .body{position:absolute;left:36px;right:36px;top:0;bottom:0;background:var(--forest);}
.stick .brand{top:26px;font-size:14px;color:var(--cream)}
.stick .product{top:46px;font-size:40px}

/* logo sheet */
.logo-sheet{left:155px;top:795px;width:376px;height:333px;background:var(--white)}
.logo-row{position:absolute;left:0;right:0;text-align:center}
.logo-row.light{top:36px;font-size:32px;color:var(--forest)}
.logo-row.dark{top:110px;height:86px;line-height:86px;font-size:32px;color:var(--cream);background:var(--forest)}
.logo-stack{position:absolute;top:211px;width:172px;height:100px;display:flex;flex-direction:column;justify-content:center;align-items:center;font-size:25px;gap:4px}
.logo-stack.dark{left:11px;background:var(--forest);color:var(--cream)}
.logo-stack.light{left:190px;color:var(--forest)}

/* flat panels */
.panel{left:798px;width:375px;height:333px}
.panel-a{top:26px}
.panel-b{top:384px;background:var(--white)}
.panel-c{top:741px}
.panel .tagline{font-size:11.5px}
.panel .weight{height:24px;line-height:24px;font-size:11px;background:var(--forest-deep)}
.panel-a .brand{top:28px;font-size:27px;color:var(--cream);line-height:1.05}
.panel-a .product{top:142px;font-size:54px}
.panel-a .tagline{top:218px}
.panel-b .brand{top:52px;font-size:20px;color:var(--forest)}
.panel-b .product{top:74px;font-size:56px;color:var(--ink)}
.panel-b .tagline{top:206px}
.panel-c .product{top:48px;font-size:56px}
.panel-c .brand{top:110px;font-size:20px;color:var(--cream)}
.panel-c .tagline{top:204px}

/* small label */
.label{left:855px;top:1101px;width:273px;height:75px;border:2px solid var(--white)}
.label .brand{top:14px;font-size:10px;color:var(--cream)}
.label .product{top:26px;font-size:30px}
</style>
</head>
<body>

<section class="pack box-front">
  <svg class="bg" viewBox="0 0 684 476" preserveAspectRatio="none" aria-hidden="true">
    <rect width="684" height="476" fill="var(--forest-deep)"/>
    <path d="M0 0H684V170C600 230 500 250 380 230C260 212 130 230 0 250Z" fill="#22391f"/>
  </svg>
  <div class="center brand">DR. NEMO FORTAL</div>
  <div class="center product">Quorabin</div>
  <p class="center tagline">Für Ihren Extra-Boost:<br>Spermidin - Ein neues Hero-Supplement<br>für Ihre Gesundheit und lange Aktivität</p>
  <div class="weight">30 Sticks a 4g - Nettogewicht 120g</div>
</section>

<section class="pack stick">
  <div class="seal l"></div>
  <div class="body">
    <div class="center brand">DR. NEMO FORTAL</div>
    <div class="center product">Quorabin</div>
  </div>
  <div class="seal r"></div>
</section>

<section class="pack logo-sheet">
  <div class="logo-row light brand">DR. NEMO FORTAL</div>
  <div class="logo-row dark brand">DR. NEMO FORTAL</div>
  <div class="logo-stack dark brand"><span>DR. NEMO</span><span>FORTAL</span></div>
  <div class="logo-stack light brand"><span>DR. NEMO</span><span>FORTAL</span></div>
</section>

<section class="pack panel panel-a">
  <svg class="bg" viewBox="0 0 375 333" preserveAspectRatio="none" aria-hidden="true">
    <rect width="375" height="333" fill="var(--forest)"/>
    <path d="M0 150C90 120 170 150 250 140C310 132 345 110 375 96V333H0Z" fill="var(--moss)"/>
  </svg>
  <div class="center brand">DR. NEMO<br>FORTAL</div>
  <div class="center product">Quorabin</div>
  <p class="center tagline">Für Ihren Extra-Boost:<br>Spermidin - Ein neues Hero-Supplement<br>für Ihre Gesundheit und lange Aktivität</p>
  <div class="weight">30 Sticks a 4g - Nettogewicht 120g</div>
</section>

<section class="pack panel panel-b">
  <svg class="bg" viewBox="0 0 375 333" preserveAspectRatio="none" aria-hidden="true">
    <rect width="375" height="333" fill="var(--white)"/>
    <path d="M0 190C70 160 150 170 230 176C300 180 345 160 375 134V333H0Z" fill="var(--moss)"/>
  </svg>
  <div class="center brand">DR. NEMO FORTAL</div>
  <div class="center product">Quorabin</div>
  <p class="center tagline">Für Ihren Extra-Boost:<br>Spermidin - Ein neues Hero-Supplement<br>für Ihre Gesundheit und lange Aktivität</p>
  <div class="weight">30 Sticks a 4g - Nettogewicht 120g</div>
</section>

<section class="pack panel panel-c">
  <svg class="bg" viewBox="0 0 375 333" preserveAspectRatio="none" aria-hidden="true">
    <rect width="375" height="333" fill="var(--moss)"/>
    <path d="M0 190C80 160 170 170 250 178C310 184 350 170 375 150V333H0Z" fill="var(--forest)"/>
  </svg>
  <div class="center product">Quorabin</div>
  <div class="center brand">DR. NEMO FORTAL</div>
  <p class="center tagline">Für Ihren Extra-Boost:<br>Spermidin - Ein neues Hero-Supplement<br>für Ihre Gesundheit und lange Aktivität</p>
  <div class="weight">30 Sticks a 4g - Nettogewicht 120g</div>
</section>

<section class="pack label">
  <svg class="bg" viewBox="0 0 273 75" preserveAspectRatio="none" aria-hidden="true">
    <rect width="273" height="75" fill="var(--forest)"/>
    <path d="M0 75V60C90 40 190 30 273 4V75Z" fill="var(--moss)"/>
  </svg>
  <div class="center brand">DR. NEMO FORTAL</div>
  <div class="center product">Quorabin</div>
</section>

</body>
</html>
```